Website Design for Law Firm

We need a fresh new website design for our client 'Torvek Legal' who specialises as a Criminal, Traffic & Civil Lawyer in Perth, Western Australia. We are looking for a very clean, professional and elegant look for the website, a presence of power and class needed as he deals with high end clients. Black, Silver and hints of gold need to run through the design without making the site look too dark. We are after a very modern, spacious web look, use of large readable text with links to social media (such as Facebook, Google+, Twitter, LinkedIn) to stand out and his contact details to be made very predominate.

Reason: Public holidays here in Australia, need more business hours to discuss designs with client.

Reason: Client needs more time to look through designs.

Reason: Client is going over last of designs. Design will be picked early next week!

Law Firm

```html
<!DOCTYPE html>
<html lang="en">
<head>
<meta charset="utf-8">
<title>Torvek Legal</title>
<link rel="stylesheet" href="https://fonts.googleapis.com/css2?family=Open+Sans:wght@300;400;600;700&family=Noticia+Text:wght@400;700&display=swap">
<style>
:root{
  --ink:#2b2a2a;
  --heading:#606060;
  --body:#7a7a7a;
  --gold:#e2b516;
  --light:#f4f4f4;
  --panel:#ececec;
  --footer:#3a3a3a;
  --white:#ffffff;
  --footer-text:#e6e6e6;
  --sky:#55acee;
}
*{box-sizing:border-box;margin:0;padding:0}
html,body{width:788px;height:1200px;overflow:hidden;background:var(--white)}
body{position:relative;font-family:"Open Sans",Arial,sans-serif;color:var(--body)}
.abs{position:absolute}

.site-header{top:0;left:0;width:788px;height:87px;background:var(--white)}
.brand{left:78px;top:38px;display:flex;align-items:center;gap:8px;z-index:3}
.brand-mark{width:14px;height:14px;background:var(--ink)}
.brand-name{font-family:"Open Sans",sans-serif;font-weight:700;font-size:26px;line-height:30px;color:var(--ink);letter-spacing:.5px}
.phone-box{left:548px;top:0;width:161px;height:34px;background:var(--panel);font-family:"Noticia Text",serif;font-size:11.5px;color:#555;display:flex;align-items:center;justify-content:center;gap:6px}
.phone-box strong{font-family:"Open Sans",sans-serif;font-weight:700;font-size:12px;color:#444;letter-spacing:.3px}
.main-nav{top:68px;left:412px;display:flex;gap:24px;font-family:"Noticia Text",serif;font-size:12px;line-height:16px;color:#444}
.main-nav .current{color:var(--gold)}

.hero{top:87px;left:0;width:788px;height:270px;background:linear-gradient(125deg,#0c0c0c 0%,#3a3a3a 22%,#d2d2d2 45%,#c4c4c4 60%,#2a2a2a 80%,#0a0a0a 100%)}
.hero-title{top:186px;left:0;width:788px;text-align:center;font-weight:300;font-size:26px;line-height:34px;color:var(--white)}
.hero-sub{top:220px;left:0;width:788px;text-align:center;font-family:"Noticia Text",serif;font-size:10px;line-height:14px;color:#333}
.hero-btn{top:253px;left:318px;width:152px;height:26px;border-radius:13px;background:#3a3a3a;color:var(--white);font-size:11px;display:flex;align-items:center;justify-content:center;gap:5px;letter-spacing:.3px}
.hero-btn span{color:var(--gold)}

.section-title{font-weight:700;font-size:16px;line-height:22px;color:var(--heading);letter-spacing:.3px}
.about-title{top:394px;left:80px}
.about-text{top:432px;left:79px;width:380px;font-size:8.4px;line-height:12.1px}
.learn-btn{top:538px;left:79px;width:88px;height:22px;background:var(--ink);color:var(--white);font-size:9.5px;display:flex;align-items:center;justify-content:center}
.news-title{top:394px;left:498px}
.news-panel{top:421px;left:497px;width:212px;height:144px;background:var(--panel);padding:0 9px}
.news-item{height:25.4px;border-bottom:1px solid #dcdcdc;display:flex;align-items:center;justify-content:space-between;font-size:7.6px;color:#444;padding:0 1px}
.news-item:last-child{border-bottom:none}
.news-item span{color:var(--gold);font-size:11px}

.services{top:632px;left:0;width:788px;height:251px;background:var(--light)}
.services-title{top:657px;left:0;width:788px;text-align:center}
.services-rule{top:678px;left:293px;width:196px;height:1px;background:var(--gold)}
.service{top:723px;width:150px;text-align:center}
.service h3{font-family:"Noticia Text",serif;font-weight:700;font-size:12px;line-height:16px;color:#444;letter-spacing:.6px}
.service svg{display:block;margin:10px auto 0}
.service p{margin-top:15px;font-size:7.3px;line-height:10px}

.social{top:926px;width:38px;height:38px;border:2px solid var(--gold);background:#e8e8e8}
.social.active{background:var(--sky);border-color:var(--sky)}

.site-footer{top:1017px;left:0;width:788px;height:183px;background:var(--footer)}
.foot-col{top:1068px;width:150px;color:var(--footer-text)}
.foot-col h4{font-weight:600;font-size:9.5px;line-height:13px;color:var(--white);margin-bottom:13px}
.foot-col li{list-style:none;font-size:7.2px;line-height:10px;margin-bottom:6px;color:var(--footer-text)}
.foot-col .addr{font-size:7.3px;line-height:13px;color:var(--footer-text)}
.foot-col .map{margin-top:4px;text-decoration:underline;color:#cfcfcf}
.foot-col .blurb{font-size:7.3px;line-height:13px;color:var(--footer-text)}
</style>
</head>
<body>
<header class="abs site-header"></header>
<div class="abs brand"><div class="brand-mark"></div><div class="brand-name">TORVEK LEGAL</div></div>
<div class="abs phone-box">Tepehone: <strong>123-555-0184</strong></div>
<nav class="abs main-nav"><span class="current">Home</span><span>Services</span><span>Our Stories</span><span>News</span><span>Contact</span></nav>

<section class="abs hero" role="img" aria-label="Black and white photograph looking up between tall dark buildings towards a pale sky"></section>
<h1 class="abs hero-title">Criminal ,Traffic &amp; Civil Lawyer</h1>
<p class="abs hero-sub">sint occaecat cupidatat non proident</p>
<div class="abs hero-btn">CONTACT <span>&#10230;</span></div>

<h2 class="abs section-title about-title">ABOUT TORVEK LEGAL</h2>
<p class="abs about-text">Excepteur sint occaecat cupidatat non proident, sunt in culpa qui officia deserunt mollit anim id est laborum. Lorem Ipsum is simply dummy text of the printing and typesetting industry. Lorem Ipsum has been the industry's standard dummy text ever since the 1500s, when an unknown printer took a galley of type and scrambled it to make a type specimen book. It has survived not only five centuries, but also the leap into electronic typesetting, remaining essentially unchanged. It was popularised in the 1960s with the release of Pressline sheets containing Lorem Ipsum passages, and more recently with desktop publishing software like Quillform Pages including versions of Lorem Ipsum.</p>
<div class="abs learn-btn">Learn More</div>

<h2 class="abs section-title news-title">LATEST NEWS</h2>
<div class="abs news-panel">
  <div class="news-item">14/10 Lorem Ipsum is dummy text<span>&#10230;</span></div>
  <div class="news-item">14/10 Lorem Ipsum is dummy text<span>&#10230;</span></div>
  <div class="news-item">14/10 Lorem Ipsum is dummy text<span>&#10230;</span></div>
  <div class="news-item">14/10 Lorem Ipsum is dummy text<span>&#10230;</span></div>
  <div class="news-item">14/10 Lorem Ipsum is dummy text<span>&#10230;</span></div>
</div>

<section class="abs services"></section>
<h2 class="abs section-title services-title">SERVICES</h2>
<div class="abs services-rule"></div>

<div class="abs service" style="left:80px">
  <h3>DUIS AUTE IRURE</h3>
  <svg width="40" height="40" viewBox="0 0 40 40" fill="none" stroke="#3a3a3a" stroke-width="2.4"><rect x="7" y="5" width="26" height="33"/><rect x="14" y="2" width="12" height="6" fill="#f4f4f4"/><path d="M12 16h16M12 22h16M12 28h16"/></svg>
  <p>Excepteur sint occaecat cupi datat non it proident, sunt in culpa qui officia dese runtorn mollit anim id est laborum.</p>
</div>
<div class="abs service" style="left:236px">
  <h3>DUIS AUTE IRURE</h3>
  <svg width="40" height="40" viewBox="0 0 40 40" fill="none" stroke="#3a3a3a" stroke-width="2.4"><path d="M20 3l12 5v14c0 8-6 12-12 15C14 34 8 30 8 22V8z"/><path d="M14 17h12M14 22h12M14 27h8"/></svg>
  <p>Excepteur sint occaecat cupi datat non it proident, sunt in culpa qui officia dese runtorn mollit anim id est laborum.</p>
</div>
<div class="abs service" style="left:397px">
  <h3>DUIS AUTE IRURE</h3>
  <svg width="44" height="40" viewBox="0 0 44 40" fill="none" stroke="#3a3a3a" stroke-width="2.4"><path d="M3 22h11l3 6h10l3-6h11v15H3z"/><path d="M9 22V3h26v19M14 10h16M14 15h16"/></svg>
  <p>Excepteur sint occaecat cupi datat non it proident, sunt in culpa qui officia dese runtorn mollit anim id est laborum.</p>
</div>
<div class="abs service" style="left:559px">
  <h3>DUIS AUTE IRURE</h3>
  <svg width="50" height="40" viewBox="0 0 50 40" fill="none" stroke="#3a3a3a" stroke-width="2.6"><path d="M2 3h16l4 5h26v30H2z"/><path d="M2 10h46"/></svg>
  <p>Excepteur sint occaecat cupi datat non it proident, sunt in culpa qui officia dese runtorn mollit anim id est laborum.</p>
</div>

<a class="abs social" style="left:275px" aria-label="Social profile one"></a>
<a class="abs social active" style="left:344px" aria-label="Social profile two"></a>
<a class="abs social" style="left:412px" aria-label="Social profile three"></a>
<a class="abs social" style="left:474px" aria-label="Social profile four"></a>

<footer class="abs site-footer"></footer>
<div class="abs foot-col" style="left:80px">
  <h4>Location</h4>
  <p class="addr">27 Harlow Crescent Avenue<br>Perth, WA 6000<br>(08) 5550 1932</p>
  <p class="addr map">see it in the map &rarr;</p>
</div>
<div class="abs foot-col" style="left:242px">
  <h4>Company</h4>
  <ul><li>Our story</li><li>Mission</li><li>Journal</li><li>Careers</li></ul>
</div>
<div class="abs foot-col" style="left:405px">
  <h4>Support</h4>
  <ul><li>FAQ</li><li>Contact us</li><li>Policies</li></ul>
</div>
<div class="abs foot-col" style="left:568px">
  <h4>Calder.</h4>
  <p class="blurb">Sed do eiusmod tempor incididunt ut labore et dolore magna aliqua.</p>
</div>
</body>
</html>
```